rk ironcraft business card metallic look

revamp the existing design but want card to have a metalic look to it

Target Market(s)

construction industry

Industry/Entity Type

constrction

Contact Information for Business Card

front of card RK Ironcraft, phone 4165550193, email rk.ironcraftt@veltrano.com and instagram account; rk_ironcraft_

Font styles to use
Other font styles liked:
• masculine

Colors

Designer to choose only greyscale colors for use in the design.

Requirements
Must have
• back side RK Ironcraft then a list of everything : Siding, ACM Panels, Standing Seam,Soffit, Fascia, Gutters,Metal,Alu,inum, Viynyl, Metal Roofs and roof repairs
Nice to have
• I would like to keep the look of the existing card with the metal grids on the front
Should not have
• Need a design in two days

```html
<!DOCTYPE html>
<html lang="en">
<head>
<meta charset="utf-8">
<title>RK Ironcraft Business Card</title>
<link href="https://fonts.googleapis.com/css2?family=Poppins:wght@500;600;700;800&display=swap" rel="stylesheet">
<style>
  :root {
    --bg: #2a2a2a;
    --card-black: #080808;
    --mesh-dark: #111111;
    --mesh-mid: #303030;
    --sheen: rgba(255,255,255,0.07);
    --steel: #8a8a8a;
    --silver: #e2e2e2;
    --name-steel: #a3a3a3;
    --text-light: #efefef;
    --text-soft: #c4c4c4;
  }
  * { box-sizing: border-box; margin: 0; padding: 0; }
  html, body { width: 1200px; height: 800px; overflow: hidden; }
  body {
    background: var(--bg);
    font-family: "Poppins", sans-serif;
    display: flex;
    align-items: center;
    justify-content: center;
    gap: 56px;
  }
  .card {
    width: 520px;
    height: 297px;
    background: var(--card-black);
    position: relative;
    overflow: hidden;
    box-shadow: 0 16px 34px rgba(0,0,0,0.5);
    border: 1px solid #3a3a3a;
  }
  .mesh-surface {
    position: absolute;
    inset: 0;
    background:
      linear-gradient(115deg, transparent 20%, var(--sheen) 42%, transparent 58%),
      radial-gradient(ellipse at 50% 38%, var(--mesh-mid) 0%, var(--mesh-dark) 58%, var(--card-black) 100%);
  }
  .silver-rule {
    position: absolute;
    left: 0; right: 0;
    height: 2px;
    background: linear-gradient(90deg, #3c3c3c 0%, var(--steel) 20%, var(--silver) 50%, var(--steel) 80%, #3c3c3c 100%);
    box-shadow: 0 1px 0 #000, 0 -1px 0 rgba(255,255,255,0.08);
  }
  .brand-name {
    position: absolute;
    left: 0; right: 0;
    text-align: center;
    font-weight: 800;
    color: var(--name-steel);
    text-transform: uppercase;
    letter-spacing: 2px;
    line-height: 1;
    white-space: nowrap;
  }
  /* front */
  .front-top {
    position: absolute;
    left: 0; right: 0; top: 0;
    height: 150px;
  }
  .rule-upper { top: 18px; }
  .rule-lower { top: 148px; }
  .front-top .brand-name { top: 60px; font-size: 48px; }
  .contact-band {
    position: absolute;
    left: 0; right: 0; top: 150px; bottom: 0;
    background: linear-gradient(180deg, #1b1b1b 0%, #0d0d0d 55%, #151515 100%);
    color: var(--text-light);
    font-weight: 600;
  }
  .rule-mid { top: 62px; opacity: 0.75; }
  .contact-row {
    position: absolute;
    display: flex;
    align-items: center;
    gap: 8px;
    white-space: nowrap;
  }
  .contact-phone { top: 18px; left: 150px; font-size: 18px; }
  .contact-social { top: 21px; left: 330px; font-size: 14px; color: var(--text-soft); font-weight: 500; }
  .contact-email { top: 90px; left: 24px; font-size: 16px; color: var(--text-soft); font-weight: 500; }
  .social-dot {
    width: 13px; height: 13px;
    border: 1.5px solid var(--text-soft);
    border-radius: 3px;
  }
  .icon { width: 17px; height: 17px; fill: var(--text-light); }
  .icon-soft { fill: var(--text-soft); }
  /* back */
  .back .brand-name { top: 82px; font-size: 50px; }
  .service-list {
    position: absolute;
    left: 24px; right: 24px; top: 172px;
    text-align: center;
    color: var(--text-light);
    font-weight: 600;
    font-size: 14px;
    line-height: 1.65;
  }
</style>
</head>
<body>
  <section class="card front">
    <div class="front-top">
      <div class="mesh-surface" role="img" aria-label="Dark perforated metal grid texture"></div>
      <div class="silver-rule rule-upper"></div>
      <p class="brand-name">RK Ironcraft</p>
      <div class="silver-rule rule-lower"></div>
    </div>
    <div class="contact-band">
      <p class="contact-row contact-phone">
        <svg class="icon" viewBox="0 0 24 24" aria-hidden="true"><path d="M6.6 10.8a15.1 15.1 0 0 0 6.6 6.6l2.2-2.2a1 1 0 0 1 1-.25 11.4 11.4 0 0 0 3.6.57 1 1 0 0 1 1 1V20a1 1 0 0 1-1 1A17 17 0 0 1 3 4a1 1 0 0 1 1-1h3.5a1 1 0 0 1 1 1c0 1.25.2 2.46.57 3.6a1 1 0 0 1-.25 1z"/></svg>
        416-555-0193
      </p>
      <p class="contact-row contact-social"><span class="social-dot"></span>rk_ironcraft_</p>
      <div class="silver-rule rule-mid"></div>
      <p class="contact-row contact-email">
        <svg class="icon icon-soft" viewBox="0 0 24 24" aria-hidden="true"><path d="M3 5h18a1 1 0 0 1 1 1v12a1 1 0 0 1-1 1H3a1 1 0 0 1-1-1V6a1 1 0 0 1 1-1zm9 7.2L4.2 7v10.8h15.6V7z"/></svg>
        rk.ironcraftt@veltrano.com
      </p>
    </div>
  </section>

  <section class="card back">
    <div class="mesh-surface" role="img" aria-label="Dark perforated metal grid texture"></div>
    <p class="brand-name">RK Ironcraft</p>
    <p class="service-list">
      Siding • ACM Panels • Standing Seam • Soffit • Fascia<br>
      Gutters • Metal • Alu • inum • Viynyl • Metal Roofs<br>
      and roof repairs
    </p>
  </section>
</body>
</html>
```